Movie Poster for Short Film Sci-Fi Drama

Kelvora Studios of North Carolina is making a new short film called "Letters Beneath the Paint".

This is short film about a lonely boy who falls in love with a girl from the past through poetry on a closet wall.

I want the poster to invoke longing and love. I want the focus of the poster to be poetry on a closet wall and I want the words from title of the movie to be part of the poetry written on the walls, but to stand out as the title somehow.

This is not a happy-go-lucky romantic comedy. The girl is from 1981 and boy is from the present era.

Because this is a promotional movie poster for a film that has not yet been shot, I do not want any humans featured in the poster. I would like to keep the focus on the handwritten poetry that sparked a romance between two teenagers decades apart in time.

I would like to have "A Kelvora Production" at the top of the poster, please.

Target Market(s)

Teenagers upward to adults.

Industry/Entity Type

Movie Production

Requirements
Must have
• Handwriting font.
Should not have
• Humans or faces; exterior walls

```html
<!DOCTYPE html>
<html lang="en">
<head>
<meta charset="utf-8">
<title>Letters Beneath the Paint — Poster</title>
<link href="https://fonts.googleapis.com/css2?family=Kaushan+Script&family=Allura&family=Mr+Dafoe&display=swap" rel="stylesheet">
<style>
  :root {
    --wall-light: #f3f2ef;
    --wall-mid: #e4e3df;
    --wall-shadow: #d3d2ce;
    --baseboard: #f6f6f4;
    --baseboard-edge: #dcdcd8;
    --floor-light: #b79478;
    --floor-dark: #7d5a43;
    --chair: #fbfbfa;
    --chair-shade: #e6e6e3;
    --title-ink: #3d5550;
    --script-ink: #1f1f1f;
  }
  html, body {
    margin: 0;
    padding: 0;
    overflow: hidden;
    background: #ffffff;
  }
  .poster {
    position: relative;
    width: 810px;
    height: 1200px;
    overflow: hidden;
    background: var(--wall-light);
  }
  .scene {
    position: absolute;
    inset: 0;
  }
  .credit {
    position: absolute;
    top: 82px;
    left: 0;
    width: 810px;
    text-align: center;
    font-family: "Mr Dafoe", cursive;
    font-size: 26px;
    color: var(--script-ink);
    margin: 0;
  }
  .title {
    position: absolute;
    inset: 0;
    margin: 0;
    font-family: "Kaushan Script", cursive;
    font-weight: 400;
    color: var(--title-ink);
    line-height: 1;
  }
  .title span {
    position: absolute;
    white-space: nowrap;
  }
  .title .word-large-first {
    left: 150px;
    top: 205px;
    font-size: 128px;
  }
  .title .word-small {
    left: 360px;
    top: 365px;
    font-size: 54px;
  }
  .title .word-large-last {
    left: 395px;
    top: 430px;
    font-size: 136px;
  }
  .tagline {
    position: absolute;
    top: 628px;
    left: 0;
    width: 810px;
    margin: 0;
    text-align: center;
    font-family: "Allura", cursive;
    font-size: 38px;
    line-height: 56px;
    color: var(--script-ink);
  }
</style>
</head>
<body>
  <main class="poster">
    <svg class="scene" width="810" height="1200" viewBox="0 0 810 1200" aria-hidden="false">
      <defs>
        <linearGradient id="wallTone" x1="0" y1="0" x2="1" y2="1">
          <stop offset="0" stop-color="var(--wall-mid)"/>
          <stop offset="0.45" stop-color="var(--wall-light)"/>
          <stop offset="1" stop-color="var(--wall-shadow)"/>
        </linearGradient>
        <linearGradient id="floorTone" x1="0" y1="0" x2="0" y2="1">
          <stop offset="0" stop-color="var(--floor-light)"/>
          <stop offset="1" stop-color="var(--floor-dark)"/>
        </linearGradient>
        <linearGradient id="chairTone" x1="0" y1="0" x2="1" y2="1">
          <stop offset="0" stop-color="var(--chair)"/>
          <stop offset="1" stop-color="var(--chair-shade)"/>
        </linearGradient>
      </defs>
      <rect class="wall" x="0" y="0" width="810" height="1002" fill="url(#wallTone)" role="img" aria-label="Photograph of a white-painted brick wall"/>
      <rect class="baseboard" x="0" y="1002" width="810" height="48" fill="var(--baseboard)"/>
      <line class="baseboard-edge" x1="0" y1="1002" x2="810" y2="1002" stroke="var(--baseboard-edge)" stroke-width="2"/>
      <rect class="floor" x="0" y="1050" width="810" height="150" fill="url(#floorTone)" role="img" aria-label="Photograph of a worn wooden plank floor"/>
      <rect class="chair" x="465" y="752" width="295" height="398" rx="40" fill="url(#chairTone)" opacity="0.85" role="img" aria-label="Photograph of a white molded shell chair on thin wire legs"/>
    </svg>

    <p class="credit">A Kelvora Production</p>

    <h1 class="title">
      <span class="word-large-first">Letters</span>
      <span class="word-small">beneath the</span>
      <span class="word-large-last">Paint</span>
    </h1>

    <p class="tagline">
      Memories fade away into the wind behind the moon.<br>
      A girl with golden eyes longs to join them very soon.
    </p>
  </main>
</body>
</html>
```